Nur Briefpapier und VK für Pflegedienst, Logo vorhanden!!!!
Zielgruppe
Wir sind ein Pflegedienst, unsere Zielgruppe sind Krankenkassen und Patienten und andere Krankenhäuser mit denen wir zusammen arbeiten.
Aufgabenstellung
modern, seriös, elitär

```html
<!DOCTYPE html>
<html lang="de">
<head>
<meta charset="utf-8">
<title>Halvor Pflegedienste – Briefpapier</title>
<link rel="stylesheet" href="https://fonts.googleapis.com/css2?family=Roboto:wght@300;400&display=swap">
<style>
  :root {
    --brand-red: #e3202b;
    --bar-grey: #4a5452;
    --text-dark: #333333;
    --paper: #ffffff;
  }
  * { margin: 0; padding: 0; box-sizing: border-box; }
  html, body { width: 854px; height: 1200px; overflow: hidden; background: var(--paper); }
  body { font-family: "Roboto", Arial, sans-serif; color: var(--text-dark); }
  .letterhead { position: relative; width: 854px; height: 1200px; background: var(--paper); }

  .top-bar { position: absolute; top: 0; left: 0; width: 854px; height: 15px; background: var(--bar-grey); }

  .brand-tab { position: absolute; top: 0; left: 708px; width: 100px; height: 204px; }
  .brand-tab svg { position: absolute; inset: 0; }
  .brand-tab__name {
    position: absolute; left: 0; width: 100px; text-align: center;
    color: #fff; font-weight: 400; font-size: 14px; letter-spacing: 0.3px;
  }
  .brand-tab__name--main { top: 56px; font-size: 22px; }
  .brand-tab__name--sub { top: 150px; }

  .sender-line {
    position: absolute; left: 101px; top: 156px;
    font-size: 10px; text-decoration: underline; text-underline-offset: 2px;
    color: var(--text-dark);
  }

  .fold-mark { position: absolute; left: 0; width: 10px; height: 1px; background: #555; }
  .fold-mark--upper { top: 362px; }
  .fold-mark--lower { top: 602px; }

  .footer-badge {
    position: absolute; left: 0; top: 1090px; width: 79px; height: 110px;
    background: var(--brand-red); color: #fff; text-align: center;
  }
  .footer-badge__name { position: absolute; top: 28px; width: 100%; font-size: 15px; }
  .footer-badge__sub { position: absolute; top: 84px; width: 100%; font-size: 9px; }

  .footer-col { position: absolute; top: 1092px; font-size: 12px; line-height: 13.5px; white-space: nowrap; }
  .footer-col p + p { margin-top: 21px; }
  .footer-col--contact { left: 108px; width: 150px; }
  .footer-col--bank { left: 267px; }

  .claim-band { position: absolute; left: 496px; top: 1148px; width: 358px; height: 52px; }
  .claim-band svg { position: absolute; inset: 0; }
  .claim-band__text {
    position: absolute; left: 36px; top: 14px;
    color: #fff; font-weight: 300; font-size: 20px; white-space: nowrap;
  }
</style>
</head>
<body>
<div class="letterhead">
  <div class="top-bar"></div>

  <div class="brand-tab">
    <svg width="100" height="204" viewBox="0 0 100 204" aria-hidden="true">
      <polygon points="0,0 100,0 100,178 50,204 0,178" fill="var(--brand-red)"/>
    </svg>
    <div class="brand-tab__name brand-tab__name--main">Halvor</div>
    <div class="brand-tab__name brand-tab__name--sub">Pflegedienste</div>
  </div>

  <div class="sender-line">Halvor Pflegedienste • Birkenhang 42 • 45127 Essen</div>

  <div class="fold-mark fold-mark--upper"></div>
  <div class="fold-mark fold-mark--lower"></div>

  <div class="footer-badge">
    <div class="footer-badge__name">Halvor</div>
    <div class="footer-badge__sub">Pflegedienste</div>
  </div>

  <div class="footer-col footer-col--contact">
    <p>Halvor Pflegedienste<br>Birkenhang 42<br>45127 Essen</p>
    <p>Tel.: 0201 - 47 30 258<br>Email: kontakt@halvor.de</p>
  </div>

  <div class="footer-col footer-col--bank">
    <p>Bankverbindung<br>IBAN: DE12 3456 7890 0000 1123 14<br>Musterbank Musterstadt</p>
    <p>Steuer-Nr.:123/4567/89<br>USt.Id.Nr.: DE1234567890</p>
  </div>

  <div class="claim-band">
    <svg width="358" height="52" viewBox="0 0 358 52" aria-hidden="true">
      <polygon points="18,0 358,0 358,52 0,52" fill="var(--brand-red)"/>
    </svg>
    <div class="claim-band__text">Schutz im Zeichen der Fürsorge</div>
  </div>
</div>
</body>
</html>
```